Business Card Design for a Personal Trainer

I need a business card design for my job as a personal trainer. It should have a unique, modern and exclusive design. On the front there should be only my logo with my name and my job. 0163/2918374 Tobias Kellinger Lindenfeldweg 14 80412 Munich Germany The most important contact information is the web adress. it can be bigger than the rest, but its not necessary. The card should be 8,5cmx5,5cm big. Font: Roboto. Colors: black, white, gray, 56c1ff.

```html
<!DOCTYPE html>
<html lang="de">
<head>
<meta charset="utf-8">
<title>Tobias Kellinger – Business Card</title>
<link rel="stylesheet" href="https://fonts.googleapis.com/css2?family=Roboto:wght@400;500&family=Work+Sans:wght@400;500&display=swap">
<style>
  :root {
    --backdrop: #e2e2e2;
    --card-white: #ffffff;
    --card-black: #050505;
    --ink: #1d1d1d;
    --banner: #231f20;
    --photo-light: #d9d9d9;
    --photo-dark: #3a3a3a;
    --paper-text: #ffffff;
  }
  html, body {
    margin: 0;
    width: 1200px;
    height: 897px;
    overflow: hidden;
    background: var(--backdrop);
  }
  .scene { position: relative; width: 1200px; height: 897px; }
  .card {
    position: absolute;
    left: 329px;
    width: 543px;
    height: 310px;
  }
  .card--front { top: 108px; background: var(--card-white); }
  .card--back  { top: 479px; background: var(--card-black); }
  .card svg { display: block; width: 543px; height: 310px; }

  .brand-name { font-family: "Roboto", sans-serif; font-weight: 400; }
  .brand-tagline { font-family: "Roboto", sans-serif; font-weight: 400; }
  .body-text { font-family: "Work Sans", sans-serif; font-weight: 400; font-size: 13.5px; fill: var(--ink); }
  .banner-name { font-family: "Work Sans", sans-serif; font-weight: 500; font-size: 14.5px; letter-spacing: 0.8px; fill: var(--paper-text); }
  .banner-role { font-family: "Work Sans", sans-serif; font-weight: 400; font-size: 12.5px; fill: var(--paper-text); }
</style>
</head>
<body>
<main class="scene">

  <section class="card card--front" aria-label="Front of business card">
    <svg viewBox="0 0 543 310" xmlns="http://www.w3.org/2000/svg">
      <defs>
        <linearGradient id="portraitTone" x1="0" y1="0" x2="0" y2="1">
          <stop offset="0" stop-color="#d9d9d9"/>
          <stop offset="0.45" stop-color="#6b6b6b"/>
          <stop offset="1" stop-color="#3a3a3a"/>
        </linearGradient>
      </defs>

      <rect class="portrait" x="29" y="20" width="212" height="290" fill="url(#portraitTone)"
            role="img" aria-label="Black and white portrait photo of the trainer, arms crossed, in a fitted training shirt"/>

      <rect class="name-banner" x="0" y="257" width="254" height="40" fill="var(--banner)"/>
      <text class="banner-name" x="127" y="275" text-anchor="middle">TOBIAS KELLINGER</text>
      <text class="banner-role" x="127" y="291" text-anchor="middle">Personal Trainer</text>

      <g class="brand">
        <rect x="386" y="45" width="26" height="26" fill="var(--ink)"/>
        <text class="brand-name" x="290" y="120" font-size="24" fill="var(--ink)"
              textLength="219" lengthAdjust="spacingAndGlyphs">TOBIAS KELLINGER</text>
        <line x1="291" y1="127" x2="323" y2="127" stroke="var(--ink)" stroke-width="1"/>
        <text class="brand-tagline" x="328" y="131" font-size="9.5" fill="var(--ink)"
              textLength="144" lengthAdjust="spacing">PERSONAL TRAINER</text>
        <line x1="477" y1="127" x2="509" y2="127" stroke="var(--ink)" stroke-width="1"/>
      </g>

      <g class="contact">
        <text class="body-text" x="291" y="200">Lindenfeldweg 14</text>
        <text class="body-text" x="291" y="222">80412 München</text>
        <text class="body-text" x="291" y="253">Phone</text>
        <text class="body-text" x="339" y="253">:</text>
        <text class="body-text" x="352" y="253">0163/2918374</text>
        <text class="body-text" x="291" y="275">Email</text>
        <text class="body-text" x="339" y="275">:</text>
        <text class="body-text" x="352" y="275">t.kellinger@postfeld.de</text>
        <text class="body-text" x="291" y="297">Web</text>
        <text class="body-text" x="339" y="297">:</text>
        <text class="body-text" x="352" y="297">www.tobiaskellinger.de</text>
      </g>
    </svg>
  </section>

  <section class="card card--back" aria-label="Back of business card">
    <svg viewBox="0 0 543 310" xmlns="http://www.w3.org/2000/svg">
      <g class="brand">
        <rect x="252" y="100" width="37" height="37" fill="var(--paper-text)"/>
        <text class="brand-name" x="131" y="207" font-size="31" fill="var(--paper-text)"
              textLength="278" lengthAdjust="spacingAndGlyphs">TOBIAS KELLINGER</text>
        <line x1="134" y1="218" x2="172" y2="218" stroke="var(--paper-text)" stroke-width="1.2"/>
        <text class="brand-tagline" x="177" y="222" font-size="12" fill="var(--paper-text)"
              textLength="186" lengthAdjust="spacing">PERSONAL TRAINER</text>
        <line x1="369" y1="218" x2="407" y2="218" stroke="var(--paper-text)" stroke-width="1.2"/>
      </g>
    </svg>
  </section>

</main>
</body>
</html>
```